Bref créative
Contract folder, Biz Card,Letter head, Fax Cov, Env,A4 Env,CD Cov&Pack,PPT
Email Sign, scratch paper
Professional
Harvinder Pal Okoro
Director
Vel Metrics Systems Private Limited
Plot No. 217 Industrial Growth Zone Phase 4 Distt- Kelmar 174 398, Punjab, India
hokoro@velmetrics.example
www.VelMetrics.example
on letter head & envelops we would prefer to mention the manufacturers we represent on Letter Head, Biz Card, A4 Env.
1) Brovane Instruments 2) Tollwick Fendor 3) Mo-Ve-Sel 4) Dovin
5) TUVO 6) Plazor 7) Orvix 8) Universal Prism Workshops 9) KV Fabrications 10) Tolbry Chemical 11) MaxiSp 12) DOR Scientific 13) VextaMol 14) KPL
1) use only logo
2) write official email info@velmetrics.example & website www.VelMetrics.example
3) Write in small "Suppliers of Chromatography Consumables & Spectroscopy Supplies"
WE ARE OPEN TO IDEAS
Vel Metrics System Private Limited Logo
vms id card sample content
logo eps format

```html
<!DOCTYPE html>
<html lang="en">
<head>
<meta charset="utf-8">
<title>Vel Metrics Systems — Stationery Set</title>
<link href="https://fonts.googleapis.com/css2?family=Open+Sans:wght@400;600&display=swap" rel="stylesheet">
<style>
:root{
  --bg:#e4e6ea;
  --paper:#f5f5f7;
  --white:#ffffff;
  --blue:#1f74c9;
  --blue-dark:#0c4c99;
  --blue-light:#3d9be6;
  --red:#d6262f;
  --ink:#3b3f47;
  --muted:#8a9099;
  --mark:#dfe5ee;
}
*{box-sizing:border-box;margin:0;padding:0}
html,body{width:1200px;height:1037px;overflow:hidden;background:var(--bg)}
body{position:relative;font-family:"Open Sans",Arial,sans-serif;color:var(--ink)}
.piece{position:absolute;background:var(--paper);box-shadow:0 2px 6px rgba(0,0,0,.18);overflow:hidden}
.logo{display:inline-flex;align-items:center;gap:.3em;font-family:"Open Sans",Arial,sans-serif;font-weight:600;color:var(--blue-dark);line-height:1;white-space:nowrap}
.logo .box{width:.55em;height:.55em;background:var(--blue-dark)}
.logo.on-blue{color:var(--white)}
.logo.on-blue .box{background:var(--white)}
.small{font-size:5.5px;line-height:1.5;color:var(--ink)}
.small.light{color:#dbe9f8}
.faint-mark{position:absolute;font-family:"Open Sans",Arial,sans-serif;font-weight:600;color:var(--mark);line-height:1;white-space:nowrap}
.band{position:absolute;left:0;right:0;bottom:0;background:linear-gradient(90deg,var(--blue-dark),var(--blue),var(--blue-light))}
.band::before{content:"";position:absolute;left:0;right:0;top:-3px;height:2px;background:var(--red)}
.footer-text{position:absolute;left:0;right:0;text-align:center;font-size:4.5px;color:var(--muted)}

/* business cards */
.card-back{background:linear-gradient(135deg,var(--blue-dark),var(--blue) 55%,var(--blue-light))}
.card-back .logo{font-size:18px;position:absolute;right:18px;bottom:30px}
.card-back .small{position:absolute;left:14px;top:14px;width:130px}
.card-front{background:var(--white)}
.card-front .logo{font-size:13px;position:absolute;left:12px;top:18px}
.card-front .name{position:absolute;left:110px;top:14px;font-size:7px;font-weight:600;color:var(--red)}
.card-front .small{position:absolute;left:110px;top:26px;width:100px}
.card-front .strip{position:absolute;left:0;right:0;bottom:0;height:6px;background:var(--blue)}

/* DL envelopes */
.dl-env .logo{font-size:13px;position:absolute;left:12px;top:16px}
.dl-env .small{position:absolute;left:12px;top:38px;width:150px}
.dl-env .faint-mark{right:14px;top:34px;font-size:26px}

/* open envelope */
.open-env{background:var(--white)}
.open-env .flap{position:absolute;left:0;top:0;width:100%;height:100%}
.open-env .logo{font-size:11px;position:absolute;left:50%;transform:translateX(-50%);top:94px}

/* letterheads */
.letterhead .logo{font-size:15px;position:absolute;left:18px;top:17px}
.letterhead .head-info{position:absolute;left:120px;top:14px;width:170px}
.letterhead .faint-mark{left:50%;top:52%;transform:translate(-50%,-50%);font-size:48px}

/* A4 envelopes */
.a4-env .flap{position:absolute;left:0;top:0;width:100%;height:70px}
.a4-env .logo{font-size:30px;position:absolute;left:50%;transform:translateX(-50%);top:90px}
.a4-env .faint-mark{left:50%;top:56%;transform:translate(-50%,-50%);font-size:54px}
</style>
</head>
<body>

<div class="piece card-back" style="left:45px;top:34px;width:216px;height:112px">
  <p class="small light">Suppliers of Chromatography Consumables &amp; Spectroscopy Supplies</p>
  <span class="logo on-blue"><span class="box"></span>VelMetrics</span>
</div>

<div class="piece card-front" style="left:272px;top:34px;width:218px;height:112px">
  <span class="logo"><span class="box"></span>VelMetrics</span>
  <p class="name">Harvinder Pal Okoro</p>
  <p class="small">Director<br>Vel Metrics Systems Private Limited<br>Plot No. 217 Industrial Growth Zone Phase 4 Distt- Kelmar 174 398<br>hokoro@velmetrics.example<br>www.VelMetrics.example</p>
  <div class="strip"></div>
</div>

<div class="piece card-back" style="left:162px;top:168px;width:222px;height:112px">
  <p class="small light">Vel Metrics Systems Private Limited<br>info@velmetrics.example<br>www.VelMetrics.example</p>
  <span class="logo on-blue"><span class="box"></span>VelMetrics</span>
</div>

<div class="piece dl-env" style="left:162px;top:314px;width:320px;height:128px">
  <span class="logo"><span class="box"></span>VelMetrics</span>
  <p class="small">Vel Metrics Systems Private Limited<br>Plot No. 217 Industrial Growth Zone Phase 4<br>Distt- Kelmar 174 398</p>
  <span class="faint-mark">VelMetrics</span>
  <div class="band" style="height:10px"></div>
</div>

<div class="piece dl-env" style="left:162px;top:456px;width:320px;height:122px">
  <span class="logo"><span class="box"></span>VelMetrics</span>
  <p class="small">Vel Metrics Systems Private Limited<br>Plot No. 217 Industrial Growth Zone Phase 4<br>Distt- Kelmar 174 398</p>
  <span class="faint-mark">VelMetrics</span>
</div>

<div class="piece open-env" style="left:162px;top:588px;width:320px;height:212px">
  <svg class="flap" viewBox="0 0 320 212" preserveAspectRatio="none" aria-hidden="true">
    <defs>
      <linearGradient id="flapGrad" x1="0" y1="0" x2="1" y2="1">
        <stop offset="0" stop-color="#0c4c99"/><stop offset=".5" stop-color="#1f74c9"/><stop offset="1" stop-color="#3d9be6"/>
      </linearGradient>
    </defs>
    <path d="M0 0 H320 V26 L160 90 L0 26 Z" fill="url(#flapGrad)"/>
    <path d="M0 212 L160 118 L320 212 Z" fill="url(#flapGrad)" opacity=".9"/>
  </svg>
  <span class="logo"><span class="box"></span>VelMetrics</span>
</div>

<div class="piece dl-env" style="left:162px;top:818px;width:320px;height:135px">
  <span class="logo"><span class="box"></span>VelMetrics</span>
  <p class="small">Vel Metrics Systems Private Limited<br>Plot No. 217 Industrial Growth Zone Phase 4<br>Distt- Kelmar 174 398</p>
  <span class="faint-mark">VelMetrics</span>
  <div class="band" style="height:10px"></div>
</div>

<div class="piece letterhead" style="left:505px;top:22px;width:322px;height:412px">
  <span class="logo"><span class="box"></span>VelMetrics</span>
  <p class="small head-info">Vel Metrics Systems Private Limited<br>Plot No. 217 Industrial Growth Zone Phase 4 Distt- Kelmar 174 398</p>
  <span class="faint-mark">VelMetrics</span>
  <p class="footer-text" style="bottom:14px">info@velmetrics.example · www.VelMetrics.example</p>
  <div class="band" style="height:8px"></div>
</div>

<div class="piece letterhead" style="left:848px;top:22px;width:318px;height:412px">
  <span class="logo"><span class="box"></span>VelMetrics</span>
  <p class="small head-info">Vel Metrics Systems Private Limited<br>Plot No. 217 Industrial Growth Zone Phase 4 Distt- Kelmar 174 398</p>
  <span class="faint-mark">VelMetrics</span>
  <p class="footer-text" style="bottom:14px">Suppliers of Chromatography Consumables &amp; Spectroscopy Supplies</p>
  <div class="band" style="height:8px"></div>
</div>

<div class="piece a4-env" style="left:515px;top:448px;width:318px;height:462px">
  <svg class="flap" viewBox="0 0 318 70" preserveAspectRatio="none" aria-hidden="true">
    <defs>
      <linearGradient id="a4Flap" x1="0" y1="0" x2="1" y2="0">
        <stop offset="0" stop-color="#0c4c99"/><stop offset=".5" stop-color="#3d9be6"/><stop offset="1" stop-color="#0c4c99"/>
      </linearGradient>
    </defs>
    <path d="M0 0 H318 V44 Q159 80 0 44 Z" fill="url(#a4Flap)"/>
  </svg>
  <span class="logo"><span class="box"></span>VelMetrics</span>
  <span class="faint-mark">VelMetrics</span>
  <p class="footer-text" style="bottom:16px">Plot No. 217 Industrial Growth Zone Phase 4 Distt- Kelmar 174 398 · www.VelMetrics.example</p>
  <div class="band" style="height:9px"></div>
</div>

<div class="piece a4-env" style="left:855px;top:468px;width:308px;height:448px">
  <svg class="flap" viewBox="0 0 308 70" preserveAspectRatio="none" aria-hidden="true">
    <path d="M0 0 H308 V44 Q154 80 0 44 Z" fill="url(#a4Flap)"/>
  </svg>
  <span class="logo"><span class="box"></span>VelMetrics</span>
  <span class="faint-mark">VelMetrics</span>
  <p class="footer-text" style="bottom:16px">Plot No. 217 Industrial Growth Zone Phase 4 Distt- Kelmar 174 398 · www.VelMetrics.example</p>
  <div class="band" style="height:9px"></div>
</div>

</body>
</html>
```